Political Association Member Newsletter

We require a professional newsletter designed that will be sent both by mail and by email (and can be posted online) to the members in our client organization. I will develop and curate the content to send to the designer but we need help with a good design.

We have two key colours: red and blue (usually on white background). The pantones are:
blue = 301C
red = 032C

The logo I have from the client is attached as well as a recent piece with contact information and social media channels noted.

The client also provided a campaign logo "Raise the Bar for 2019" that will accompany copy for membership and donation which will follow.

Two preliminary content pieces are also included here: a flyer for a bbq and the "Regional Forum Digest" article.

Political

Sans Serif

• Space for pictures - uploaded below.

```html
<!DOCTYPE html>
<html lang="en">
<head>
<meta charset="utf-8">
<title>Regional Forum Digest</title>
<link href="https://fonts.googleapis.com/css2?family=Gelasio:ital,wght@1,400&family=Roboto+Condensed:wght@700&display=swap" rel="stylesheet">
<style>
:root{
  --party-blue:#1d4f8c;
  --party-red:#ef3340;
  --frame-red:#c8143c;
  --band-red:#d41f45;
  --page-top:#eeeeee;
  --page-bottom:#ffffff;
  --white:#ffffff;
}
*{margin:0;padding:0;box-sizing:border-box}
html,body{width:1019px;height:1200px;overflow:hidden}
body{
  position:relative;
  background:linear-gradient(180deg,var(--page-top) 0%,var(--page-top) 40%,var(--page-bottom) 100%);
  font-family:"Gelasio",Georgia,serif;
}
.photo-strip{position:absolute;top:28px;left:46px;width:924px;height:200px}
.photo-frame{
  position:absolute;top:0;height:200px;
  background:var(--frame-red);padding:10px;
  box-shadow:5px 6px 8px rgba(0,0,0,.45);
}
.photo-frame:nth-child(1){left:0;width:302px}
.photo-frame:nth-child(2){left:311px;width:304px}
.photo-frame:nth-child(3){left:622px;width:302px}
.photo{width:100%;height:100%}
.photo--members{background:linear-gradient(135deg,#6d6a64,#3a4150 60%,#8a7f70)}
.photo--tables{background:linear-gradient(180deg,#2a3560,#3b3a44 50%,#6b6560)}
.photo--stage{background:linear-gradient(180deg,#0f1c55,#2340a8 45%,#141a30)}

.letter{
  position:absolute;left:49px;top:326px;width:926px;
  color:var(--party-blue);font-style:italic;font-size:21.5px;line-height:30.6px;
  text-align:justify;
}
.letter p{margin-bottom:30.6px}
.quote-mark{
  font-family:"Roboto Condensed",Arial,sans-serif;font-style:normal;font-weight:700;
  color:var(--party-red);font-size:150px;line-height:1;
}
.quote-mark--open{float:left;width:83px;height:86px;margin-top:-12px;line-height:120px}
.quote-mark--close{float:right;width:80px;height:86px;margin:36px 0 0 14px;line-height:120px;text-align:right}
.signature{line-height:30.6px}
.signature .name{color:var(--party-red)}

.footer-rule{position:absolute;left:0;top:1082px;width:1019px;height:6px;background:var(--band-red)}
.footer{
  position:absolute;left:0;top:1097px;width:1019px;height:103px;background:var(--band-red);
  display:flex;align-items:center;padding-left:48px;
  font-family:"Roboto Condensed",Arial,sans-serif;font-weight:700;font-size:16px;color:var(--white);
}
.footer-item{display:flex;align-items:center;gap:10px}
.footer-item .dot{width:22px;height:22px;border-radius:50%;background:var(--white);flex:none}
.footer-item--party{width:258px;line-height:17px}
.footer-item--party .dot{width:40px;height:40px}
.footer-item--social{width:316px}
.footer-item--handle{width:176px}
</style>
</head>
<body>
<section class="photo-strip">
  <div class="photo-frame"><div class="photo photo--members" role="img" aria-label="Photo of three party members standing together at the convention"></div></div>
  <div class="photo-frame"><div class="photo photo--tables" role="img" aria-label="Photo of delegates seated around a long convention table"></div></div>
  <div class="photo-frame"><div class="photo photo--stage" role="img" aria-label="Photo of the convention hall stage with large screens"></div></div>
</section>

<article class="letter">
  <span class="quote-mark quote-mark--open" aria-hidden="true">&ldquo;</span>
  <p>It’s my pleasure to introduce myself as the newest member of Regional Forum from Alberta. &nbsp;I will join Joanne Harlow from Calgary representing the views of members from across the province. &nbsp;I’ve met many of you over the years, in particular during my three years as EDA President in Riverside Centre, and I’m looking forward to working for you again.</p>
  <p>The 2016 Heritage National Convention was a remarkable success. &nbsp;Our Party took important steps toward building a foundation for a broader coalition of conservatives, we said thank you to former Prime Minister Richard Halden, and we heard compelling narratives for what lies ahead.</p>
  <p>We also elected Martin Keyes as our new Party President. &nbsp;Martin is a Vancouver-based lawyer with a keen sense of the issues that need to be addressed in the months ahead. &nbsp;I trust you’ll join me in congratulating Martin!</p>
  <p><span class="quote-mark quote-mark--close" aria-hidden="true">&rdquo;</span>I know many of you have a busy summer ahead, but I encourage you to stay engaged with your EDA and our Party. &nbsp;Join us at the Northern Alberta Heritage BBQ on August 13, volunteer for a leadership campaign, or encourage your neighbours to become members and join our team. &nbsp;Together we can put out Party in a position to bring better government back to our great country!</p>
  <div class="signature">
    <div class="name">Daniel Ferrow</div>
    <div>Regional Forum</div>
    <div>danielferrow@heritageparty.ca</div>
  </div>
</article>

<div class="footer-rule"></div>
<footer class="footer">
  <div class="footer-item footer-item--party"><span class="dot"></span><span>Heritage Party of Canada,<br>Riverside Centre</span></div>
  <div class="footer-item footer-item--social"><span class="dot"></span><span>Riverside Centre Heritage Association</span></div>
  <div class="footer-item footer-item--handle"><span class="dot"></span><span>@RiversideHPC</span></div>
  <div class="footer-item footer-item--web">
    <svg width="20" height="30" viewBox="0 0 20 30" aria-hidden="true"><path d="M2 2 L2 24 L7 19 L11 28 L14 26.5 L10 18 L17 18 Z" fill="#fff" stroke="#333" stroke-width="1.2" stroke-linejoin="round"/></svg>
    <span>www.heritageparty.ca</span>
  </div>
</footer>
</body>
</html>
```